Leadership Conference Graphic Design Image

The Theme of our Conference is "Navigating Change. Driving Success." Attached is an AI example - What we are looking for is something along the lines of this image, but with realistic roads, a realistic semi truck (without being able to tell the make of the semi truck) and with the semi truck leaving dark skies and heading towards positive sunnier type skies. Please don't use the "Pinecrest Haulers Guild Yearly Convention" verbiage - Our event is called "Leadership Conference and Vendor Showcase". I've also attached our logo which we would like on the image as well - And we would like both vertical and horizontal designs. We will be using this on our stage and in printed materials.

```html
<!DOCTYPE html>
<html lang="en">
<head>
<meta charset="utf-8">
<title>Navigating Change. Driving Success. – Leadership Conference and Vendor Showcase</title>
<link rel="stylesheet" href="https://fonts.googleapis.com/css2?family=Montserrat:wght@400;500;800;900&display=swap">
<style>
  :root {
    --storm: #141b2b;
    --storm-mid: #2c3347;
    --dusk: #6f5b8f;
    --amber: #e79a3c;
    --sun: #fbe3a0;
    --road: #1c1d2a;
    --white: #ffffff;
    --gold-light: #f2e15a;
    --gold-dark: #a88a12;
    --alert: #f2d23a;
    --alert-edge: #c9861a;
    --pin: #e23a2e;
    --compass: #2fc2a6;
    --shadow: rgba(10, 10, 20, 0.75);
  }
  html, body {
    margin: 0;
    padding: 0;
    width: 1200px;
    height: 783px;
    overflow: hidden;
    background: var(--storm);
  }
  .poster {
    position: relative;
    width: 1200px;
    height: 783px;
    overflow: hidden;
    font-family: "Montserrat", sans-serif;
  }
  .scene {
    position: absolute;
    inset: 0;
    background:
      radial-gradient(ellipse 420px 300px at 1080px 430px, var(--sun) 0%, rgba(251,227,160,0.55) 35%, rgba(231,154,60,0) 75%),
      linear-gradient(180deg, rgba(0,0,0,0) 60%, rgba(28,29,42,0.85) 80%, var(--road) 100%),
      linear-gradient(90deg, var(--storm) 0%, var(--storm-mid) 25%, var(--dusk) 50%, var(--amber) 78%, #f3b65a 100%);
  }
  .icon {
    position: absolute;
  }
  .icon-compass { left: 185px; top: 95px; width: 115px; height: 135px; }
  .icon-alert   { left: 543px; top: 42px; width: 104px; height: 102px; }
  .icon-pin     { left: 875px; top: 112px; width: 78px; height: 118px; }

  .headline {
    position: absolute;
    margin: 0;
    white-space: nowrap;
    font-weight: 900;
    font-size: 78px;
    line-height: 1;
    letter-spacing: 0;
    transform-origin: left top;
  }
  .headline-change {
    top: 273px;
    left: 219px;
    color: var(--white);
    text-shadow: 3px 4px 6px var(--shadow);
    transform: scaleX(0.85);
  }
  .headline-success {
    top: 342px;
    left: 285px;
    background: linear-gradient(180deg, var(--gold-light) 0%, #d8bf22 55%, var(--gold-dark) 100%);
    -webkit-background-clip: text;
    background-clip: text;
    color: transparent;
    filter: drop-shadow(3px 4px 4px var(--shadow));
    transform: scaleX(0.89);
  }
  .event-name {
    position: absolute;
    top: 437px;
    left: 0;
    width: 1234px;
    margin: 0;
    white-space: nowrap;
    text-align: center;
    font-weight: 400;
    font-size: 40px;
    line-height: 45px;
    letter-spacing: 1px;
    color: var(--white);
    text-shadow: 2px 3px 4px var(--shadow);
    transform: scaleX(0.88);
    transform-origin: 617px top;
  }
  .org-name {
    position: absolute;
    left: 36px;
    top: 690px;
    margin: 0;
    white-space: nowrap;
    font-weight: 800;
    font-size: 22px;
    line-height: 26px;
    color: var(--white);
  }
</style>
</head>
<body>
<main class="poster">
  <div class="scene" role="img" aria-label="Photograph of a white semi truck driving down a highway from dark storm clouds on the left toward a bright golden sunset on the right, overlaid with a glowing network world map"></div>

  <svg class="icon icon-compass" viewBox="0 0 115 135" aria-hidden="true">
    <circle cx="33" cy="12" r="8" fill="none" stroke="#e9eef2" stroke-width="5"/>
    <circle cx="58" cy="78" r="56" fill="#dfe6ea"/>
    <circle cx="58" cy="78" r="47" fill="var(--compass)"/>
    <circle cx="58" cy="78" r="30" fill="none" stroke="#e9f6f2" stroke-width="3"/>
    <polygon points="58,44 64,72 58,78 52,72" fill="var(--pin)"/>
    <polygon points="58,112 64,84 58,78 52,84" fill="#f2f2f2"/>
    <polygon points="24,78 52,72 58,78 52,84" fill="#f2f2f2"/>
    <polygon points="92,78 64,72 58,78 64,84" fill="var(--pin)"/>
  </svg>

  <svg class="icon icon-alert" viewBox="0 0 104 102" aria-hidden="true">
    <path d="M52 6 Q60 6 64 14 L98 78 Q102 92 88 94 L16 94 Q2 92 6 78 L40 14 Q44 6 52 6 Z" fill="var(--alert-edge)"/>
    <path d="M52 2 Q60 2 64 10 L98 72 Q102 86 88 88 L16 88 Q2 86 6 72 L40 10 Q44 2 52 2 Z" fill="var(--alert)"/>
    <rect x="45" y="26" width="14" height="34" rx="6" fill="var(--alert-edge)"/>
    <rect x="45" y="66" width="14" height="12" rx="5" fill="var(--alert-edge)"/>
  </svg>

  <svg class="icon icon-pin" viewBox="0 0 78 118" aria-hidden="true">
    <path d="M39 2 C18 2 2 18 2 38 C2 62 39 116 39 116 C39 116 76 62 76 38 C76 18 60 2 39 2 Z" fill="var(--pin)"/>
    <circle cx="39" cy="38" r="15" fill="#f7f1ee"/>
  </svg>

  <h1 class="headline headline-change">NAVIGATING CHANGE.</h1>
  <p class="headline headline-success">DRIVING SUCCESS.</p>
  <p class="event-name">LEADERSHIP CONFERENCE AND<br>VENDOR SHOWCASE</p>

  <p class="org-name">PINECREST<br>HAULERS GUILD</p>
</main>
</body>
</html>
```